Austrian finance und insurance broker needs business card design

We Need a serious looking Design for Business Card. we consult private and corporates customers in finance and insurance questions. the final design should express security and experience. We consult customers in questions of loans, Investments and insurance and have a wide range of Banks to offer. We compare several offers and select the best for our customers.

Target Market(s)

private and coporate customers with efforts in Money and insurance

Industry/Entity Type

Insurance Broker

Contact Information for Business Card

Bernhard Aigner
Geschäftsführer
staatl. geprüfter Vermögensberater und Versicherungsmakler
Tel: 0664 521 8409
office@der-brandl.at
www.der-brandl.at
Leopold Hainz Gasse 14
2183 Melkstetten
GISA Nr. 48270315 u. 51736048 (backside)

Font styles to use
Serif
Sans Serif

Requirements
Must have
• logo (designcrowd zip) and all Details
Nice to have
• makler logo design, maybe a 2 coloured Version is possible

```html
<!DOCTYPE html>
<html lang="de">
<head>
<meta charset="utf-8">
<title>Orvalin Vermögensberatung – Visitenkarte</title>
<link rel="stylesheet" href="https://fonts.googleapis.com/css2?family=Nunito:wght@600;700;800&family=Roboto+Condensed:wght@400&family=Roboto:wght@400&display=swap">
<style>
  :root {
    --brand-blue: #0a5197;
    --brand-blue-dark: #074684;
    --ink-grey: #4a4d52;
    --band-grey: #5e6166;
    --paper: #f4f4f4;
    --paper-shade: #e6e6e6;
    --badge-red: #b3121c;
    --stage: #c9c9c9;
    --white: #ffffff;
  }
  * { margin: 0; padding: 0; box-sizing: border-box; }
  html, body {
    width: 1200px; height: 576px; overflow: hidden;
    background: var(--stage);
  }
  .card {
    position: absolute; top: 138px;
    width: 482px; height: 294px;
    border-radius: 12px; overflow: hidden;
  }
  /* Back side */
  .card--back {
    left: 82px;
    background: linear-gradient(180deg, var(--brand-blue) 0%, var(--brand-blue-dark) 100%);
    color: var(--white);
  }
  .back-mark {
    position: absolute; left: 40px; top: 126px; width: 126px;
    text-align: center;
    font: 800 26px/1 "Nunito", sans-serif;
    color: var(--white);
  }
  .back-divider {
    position: absolute; left: 176px; top: 92px;
    width: 2px; height: 92px; background: var(--white);
  }
  .back-company {
    position: absolute; left: 188px; top: 118px;
    font: 700 17px/1 "Nunito", sans-serif;
  }
  .back-company small, .front-company small { font-size: 0.78em; }
  .back-tagline {
    position: absolute; left: 188px; top: 142px;
    font: 700 13.5px/1 "Nunito", sans-serif;
  }
  .back-gisa {
    position: absolute; left: 0; right: 0; top: 264px;
    text-align: center;
    font: 600 13px/1 "Nunito", sans-serif;
    letter-spacing: 0.2px;
  }
  /* Front side */
  .card--front {
    left: 602px;
    background: linear-gradient(180deg, var(--paper) 0%, var(--paper-shade) 100%);
  }
  .front-company {
    position: absolute; left: 24px; top: 24px;
    font: 800 21px/1 "Nunito", sans-serif;
    color: var(--brand-blue);
  }
  .front-tagline {
    position: absolute; left: 24px; top: 52px;
    font: 700 15.5px/1 "Nunito", sans-serif;
    color: var(--ink-grey);
  }
  .front-art { position: absolute; left: 0; top: 0; }
  .front-mark {
    position: absolute; left: 300px; top: 134px; width: 176px;
    text-align: center;
    font: 800 32px/1 "Nunito", sans-serif;
    color: var(--ink-grey);
  }
  .holder {
    position: absolute; left: 24px; top: 98px; color: var(--white);
  }
  .holder-name { font: 800 19px/1 "Nunito", sans-serif; margin-bottom: 8px; }
  .holder-role { font: 400 11.5px/15.5px "Roboto Condensed", sans-serif; }
  .contact-list {
    position: absolute; left: 24px; top: 174px; list-style: none;
    color: var(--white);
    font: 400 13px/16px "Roboto", sans-serif;
  }
  .contact-list li { display: flex; align-items: center; gap: 10px; }
  .contact-list svg { width: 12px; height: 12px; fill: var(--white); }
  .partner-badge {
    position: absolute; left: 26px; top: 245px;
    width: 36px; height: 36px; border-radius: 50%;
    background: var(--badge-red);
  }
  .front-address {
    position: absolute; right: 30px; top: 265px;
    font: 400 12.5px/1 "Roboto", sans-serif;
    color: var(--ink-grey);
  }
</style>
</head>
<body>

<section class="card card--back" aria-label="Rückseite">
  <div class="back-mark">Orvalin</div>
  <div class="back-divider"></div>
  <div class="back-company">Vermögensberatung <small>GmbH</small></div>
  <div class="back-tagline">Finanzieren, Versichern, Vorsorgen</div>
  <div class="back-gisa">GISA Nr. 48270315 u. 51736048</div>
</section>

<section class="card card--front" aria-label="Vorderseite">
  <svg class="front-art" width="482" height="294" viewBox="0 0 482 294">
    <rect x="0" y="81" width="400" height="151" fill="var(--brand-blue)"/>
    <rect x="446" y="81" width="36" height="151" fill="var(--band-grey)"/>
    <circle cx="388" cy="150" r="88" fill="var(--paper)" stroke="var(--brand-blue)" stroke-width="5"/>
  </svg>

  <div class="front-company">Vermögensberatung <small>GmbH</small></div>
  <div class="front-tagline">Finanzieren, Versichern, Vorsorgen</div>

  <div class="holder">
    <div class="holder-name">Bernhard Aigner</div>
    <div class="holder-role">Geschäftsführer<br>Staatl. Geprüfter Vermögensberater<br>und Versicherungsmakler</div>
  </div>

  <ul class="contact-list">
    <li><svg viewBox="0 0 24 24"><path d="M6.6 10.8a15.1 15.1 0 0 0 6.6 6.6l2.2-2.2c.3-.3.7-.4 1-.2 1.1.4 2.3.6 3.6.6.6 0 1 .4 1 1V20c0 .6-.4 1-1 1A17 17 0 0 1 3 4c0-.6.4-1 1-1h3.5c.6 0 1 .4 1 1 0 1.3.2 2.5.6 3.6.1.3 0 .7-.2 1z"/></svg>0664 521 8409</li>
    <li><svg viewBox="0 0 24 24"><path d="M2 5h20v14H2zm2 2v.4l8 5 8-5V7zm0 2.8V17h16V9.8l-8 5z"/></svg>office@der-brandl.at</li>
    <li><svg viewBox="0 0 24 24"><path d="M12 2a10 10 0 1 0 0 20 10 10 0 0 0 0-20zm6.9 6h-3a15 15 0 0 0-1.3-3.9A8 8 0 0 1 18.9 8zM12 4c.8 1.2 1.5 2.5 1.9 4h-3.8c.4-1.5 1.1-2.8 1.9-4zM4.3 14a8 8 0 0 1 0-4h3.4a16 16 0 0 0 0 4zm.8 2h3a15 15 0 0 0 1.3 3.9A8 8 0 0 1 5.1 16zm3-8h-3a8 8 0 0 1 4.3-3.9C8.8 5.3 8.4 6.6 8.1 8zM12 20c-.8-1.2-1.5-2.5-1.9-4h3.8c-.4 1.5-1.1 2.8-1.9 4zm2.3-6H9.7a14 14 0 0 1 0-4h4.6a14 14 0 0 1 0 4zm.3 5.9c.6-1.2 1-2.5 1.3-3.9h3a8 8 0 0 1-4.3 3.9zm1.7-5.9a16 16 0 0 0 0-4h3.4a8 8 0 0 1 0 4z"/></svg>www.der-brandl.at</li>
  </ul>

  <div class="front-mark">Orvalin</div>

  <div class="partner-badge" role="img" aria-label="Partnerabzeichen Versicherungsmakler"></div>
  <div class="front-address">Leopold Hainz Gasse 14 2183 Melkstetten</div>
</section>

</body>
</html>
```